Radiant Harbor Holdings business card

We are a real estate advisory and investment company. We are specialized in assisting high networth individuals to invest in real estate overseas. We deliver a very personalized service, anticipating all the potential challenges an investor can face, and making it easy and safe for them. We also co-invest with our clients, assuring them that each project will be looked after as it is our own, and at the same time giving them the extra booth on confidence to invest.

We need a business card design. The business card must have a very premium, high-end look, reflecting principles like "commitment", "trust" and "timeless (but contemporary)". We look for long term relationships with our clients, and we grow with their referrals. We are all about conquering the confidence of the clients by always delivering above the expectations performance.

Target Market(s)

High net worth individuals.

Industry/Entity Type

Real Estate

Contact Information for Business Card

Please consider places on the business card for:

Name
Function (bellow name in smaller size text)

Mobile phone
E-mail
Skype ID
WeChat ID

Adress (3 lines)

Also include the following locations references:
PORTUGAL * DUBAI * HONG KONG

Website: www.rhholdings.example

Requirements
Must have
• Company Logo

```html
<!DOCTYPE html>
<html lang="en">
<head>
<meta charset="UTF-8">
<title>Radiant Harbor Holdings – Business Card</title>
<link href="https://fonts.googleapis.com/css2?family=Roboto:wght@300;400&display=swap" rel="stylesheet">
<style>
  :root {
    --bg: #2b2b2d;
    --card: #ffffff;
    --brand-blue: #29a9e1;
    --rule-blue: #9fd6ef;
    --text-grey: #5d5f63;
    --swoosh-grey: #8a8b8f;
  }
  * { margin: 0; padding: 0; box-sizing: border-box; }
  html, body {
    width: 1200px; height: 900px; overflow: hidden;
    background: var(--bg);
    font-family: 'Roboto', Arial, sans-serif;
    color: var(--text-grey);
  }
  .stage { position: relative; width: 1200px; height: 900px; }
  .card {
    position: absolute; left: 250px;
    width: 700px; height: 400px;
    background: var(--card);
    overflow: hidden;
  }
  .card--front { top: 33px; }
  .card--back { top: 467px; }

  /* Wordmark */
  .wordmark {
    display: flex; align-items: center; gap: 10px;
    font-weight: 400; color: var(--brand-blue);
    letter-spacing: 1.5px; text-transform: uppercase;
  }
  .wordmark__dot {
    width: 14px; height: 14px; border-radius: 50%;
    background: var(--brand-blue);
  }

  /* Front */
  .front__brand {
    position: absolute; left: 0; right: 0; top: 140px;
    display: flex; flex-direction: column; align-items: center;
  }
  .front__brand .wordmark { font-size: 26px; }
  .front__locations {
    margin-top: 18px; font-size: 16px; font-weight: 300;
    letter-spacing: 1px; color: var(--text-grey);
  }
  .front__website {
    position: absolute; left: 0; right: 0; bottom: 52px;
    text-align: center; font-size: 14px; letter-spacing: 2.5px;
    font-weight: 300;
  }
  .front__website .accent { color: var(--brand-blue); }

  /* Back */
  .back__brand { position: absolute; left: 46px; top: 74px; }
  .back__brand .wordmark { font-size: 22px; }
  .back__rule {
    position: absolute; left: 200px; right: 170px; top: 214px;
    height: 1px; background: var(--rule-blue);
  }
  .back__identity {
    position: absolute; right: 44px; top: 182px; text-align: right;
    color: var(--brand-blue);
  }
  .back__name { font-size: 21px; font-weight: 400; }
  .back__role { font-size: 14px; font-weight: 400; }
  .back__tab {
    position: absolute; right: 0; top: 176px;
    width: 8px; height: 26px; background: var(--brand-blue);
  }
  .back__contacts {
    position: absolute; left: 200px; top: 240px;
    list-style: none; font-size: 15px; font-weight: 300; line-height: 20px;
  }
  .back__contacts li { display: flex; align-items: center; gap: 14px; }
  .contact-icon { width: 14px; height: 14px; flex: none; }
  .back__address {
    position: absolute; right: 44px; top: 254px; text-align: right;
    font-size: 14px; font-weight: 300; line-height: 19px;
  }
  .back__swoosh { position: absolute; left: 0; bottom: 0; width: 700px; height: 140px; }
</style>
</head>
<body>
<main class="stage">

  <section class="card card--front" aria-label="Card front">
    <div class="front__brand">
      <div class="wordmark"><span class="wordmark__dot"></span>Radiant Harbor Holdings</div>
      <p class="front__locations">PORTUGAL * DUBAI * HONG KONG</p>
    </div>
    <p class="front__website">www.<span class="accent">rhholdings</span>.example</p>
  </section>

  <section class="card card--back" aria-label="Card back">
    <div class="back__brand">
      <div class="wordmark"><span class="wordmark__dot"></span>Radiant Harbor Holdings</div>
    </div>

    <div class="back__tab"></div>
    <div class="back__identity">
      <p class="back__name">Daniel Marsh</p>
      <p class="back__role">President</p>
    </div>
    <div class="back__rule"></div>

    <ul class="back__contacts">
      <li>
        <svg class="contact-icon" viewBox="0 0 14 14" aria-hidden="true"><rect x="3" y="0.5" width="8" height="13" rx="1.5" fill="none" stroke="var(--brand-blue)" stroke-width="1.3"/><rect x="4.5" y="2.5" width="5" height="7" fill="var(--brand-blue)"/></svg>
        555.014.2290
      </li>
      <li>
        <svg class="contact-icon" viewBox="0 0 14 14" aria-hidden="true"><rect x="0.5" y="2.5" width="13" height="9" fill="var(--brand-blue)"/><path d="M0.5 2.5 L7 8 L13.5 2.5" fill="none" stroke="#fff" stroke-width="1.2"/></svg>
        DMarsh@rhholdings.example
      </li>
      <li>
        <svg class="contact-icon" viewBox="0 0 14 14" aria-hidden="true"><circle cx="7" cy="7" r="6" fill="var(--brand-blue)"/></svg>
        Daniel Marsh
      </li>
      <li>
        <svg class="contact-icon" viewBox="0 0 14 14" aria-hidden="true"><circle cx="7" cy="7" r="6" fill="var(--brand-blue)"/></svg>
        Daniel Marsh
      </li>
    </ul>

    <address class="back__address" style="font-style:normal">
      2750 N. Alder Ave.<br>Mesa, AZ 85201
    </address>

    <svg class="back__swoosh" viewBox="0 0 700 140" preserveAspectRatio="none" aria-hidden="true">
      <path d="M300 140 C 460 110, 600 70, 700 20 L700 36 C 600 82, 470 118, 360 140 Z" fill="var(--swoosh-grey)"/>
      <path d="M0 122 C 250 118, 520 90, 700 36 L700 140 L0 140 Z" fill="var(--brand-blue)"/>
      <path d="M0 122 C 250 118, 520 90, 700 36" fill="none" stroke="#fff" stroke-width="3"/>
    </svg>
  </section>

</main>
</body>
</html>
```